Real Estate "For Sale" Sign for construction company

We need a sign that we can use to hang on a post and place on the road when we sell a property. The sign will be simple and will need to mainly feature our logo (files attached), as well as the words "For Sale", and then our phone number "(555) 617 3489". The sign will hang on a post that'll look something like the attached picture.

Target Market(s)

Home buyers

Industry/Entity Type

Real Estate

Font styles to use
Serif
Sans Serif

Colors
0054AA
0677BA
7BADD7
CADEEF
E8F1F8
0094D4
00A9DD
6FCCEA
C7EBF8
E9F6FB

Requirements
Must have
• For Sale & our phone number

```html
<!DOCTYPE html>
<html lang="en">
<head>
<meta charset="utf-8">
<title>Harbor Lane Realty – For Sale Sign</title>
<link rel="stylesheet" href="https://fonts.googleapis.com/css2?family=Spectral+SC:wght@800&family=Lexend:wght@500;600&display=swap">
<style>
  :root {
    --sky: #8fd8f8;
    --navy: #14204c;
    --page: #ffffff;
    --white: #ffffff;
  }
  * { margin: 0; padding: 0; box-sizing: border-box; }
  html, body {
    width: 1200px;
    height: 800px;
    overflow: hidden;
    background: var(--page);
  }
  .canvas {
    width: 1200px;
    height: 800px;
    display: flex;
    align-items: center;
    justify-content: center;
  }
  .sign {
    position: relative;
    width: 460px;
    height: 467px;
    background: var(--sky);
    border-radius: 6px;
    overflow: hidden;
    display: flex;
    flex-direction: column;
  }
  .corner {
    position: absolute;
    top: 12px;
    width: 29px;
    height: 29px;
  }
  .corner--left { left: 12px; }
  .corner--right { right: 12px; }
  .sign__brand {
    height: 175px;
    flex: none;
    display: flex;
    align-items: center;
    justify-content: center;
    gap: 12px;
    padding-top: 18px;
  }
  .brand__mark {
    width: 18px;
    height: 18px;
    background: var(--navy);
    flex: none;
  }
  .brand__name {
    font-family: "Lexend", sans-serif;
    font-weight: 500;
    font-size: 31px;
    color: var(--navy);
    white-space: nowrap;
  }
  .sign__band {
    height: 133px;
    flex: none;
    background: var(--navy);
    display: flex;
    align-items: center;
    justify-content: center;
  }
  .band__title {
    font-family: "Spectral SC", serif;
    font-weight: 800;
    font-size: 68px;
    color: var(--white);
    letter-spacing: 2px;
    line-height: 1;
  }
  .sign__contact {
    flex: 1;
    display: flex;
    flex-direction: column;
    align-items: center;
    justify-content: center;
    color: var(--navy);
    font-family: "Lexend", sans-serif;
    padding-bottom: 4px;
  }
  .contact__lead {
    font-weight: 500;
    font-size: 28px;
    line-height: 1;
    margin-bottom: 26px;
  }
  .contact__phone {
    font-weight: 600;
    font-size: 50px;
    letter-spacing: 0.5px;
    line-height: 1;
  }
</style>
</head>
<body>
  <main class="canvas">
    <section class="sign" aria-label="For sale sign">
      <svg class="corner corner--left" viewBox="0 0 32 32" aria-hidden="true">
        <polygon points="0,0 32,0 0,32" fill="var(--navy)"/>
      </svg>
      <svg class="corner corner--right" viewBox="0 0 32 32" aria-hidden="true">
        <polygon points="0,0 32,0 32,32" fill="var(--navy)"/>
      </svg>

      <header class="sign__brand">
        <span class="brand__mark" aria-hidden="true"></span>
        <span class="brand__name">Harbor Lane Realty</span>
      </header>

      <div class="sign__band">
        <h1 class="band__title">FOR SALE</h1>
      </div>

      <div class="sign__contact">
        <p class="contact__lead">Call Us Today At:</p>
        <p class="contact__phone">(555) 617-3489</p>
      </div>
    </section>
  </main>
</body>
</html>
```